Designer my sauce product Label

Hi there, I looking for someone to design my BBQ sauce bottle, I need it to be eye catching, creative and new modern. I have a standard 150ml bottle. The suace is called velquino sauce. I would like my logo to be on the bottle but not to large, I have also added examples of other designs that I like, My label has to be current with the market at the moment. Bottle attached

Target Market(s)

My target market is the early 20's to eary 30's, people that liek to eat and try new things

Industry/Entity Type

Fast Food Restaurant

Requirements
Must have
• Must have colour and be creative
Nice to have
• It would be nice to see some little images
Should not have
• N/A

```html
<!DOCTYPE html>
<html lang="en">
<head>
<meta charset="utf-8">
<title>Velquino BBQ Sauce Label</title>
<link rel="stylesheet" href="https://fonts.googleapis.com/css2?family=Alfa+Slab+One&family=Oswald:wght@500;700&family=Rye&display=swap">
<style>
  :root {
    --backdrop: #ecedef;
    --sauce-dark: #2e0f0c;
    --sauce-deep: #4a1712;
    --label-red: #c8281f;
    --ornament-light: #f1d9d4;
    --ornament-red: #b3231b;
    --panel-dark: #361512;
    --ink-white: #f6efe9;
    --ink-red: #d5342a;
  }
  * { box-sizing: border-box; margin: 0; padding: 0; }
  html, body {
    width: 863px;
    height: 1200px;
    overflow: hidden;
    background: var(--backdrop);
  }
  .canvas {
    position: relative;
    width: 863px;
    height: 1200px;
    display: flex;
    flex-direction: column;
    align-items: center;
    justify-content: center;
    gap: 40px;
  }
  .neck-seal {
    width: 150px;
    height: 150px;
    border-radius: 50%;
    background: var(--sauce-dark);
    border: 3px solid var(--ink-white);
    display: flex;
    align-items: center;
    justify-content: center;
  }
  .neck-seal__name {
    font-family: "Oswald", sans-serif;
    font-weight: 700;
    font-size: 24px;
    letter-spacing: 2px;
    color: var(--ink-white);
  }
  .body-label {
    position: relative;
    width: 560px;
    height: 760px;
    background: linear-gradient(90deg, var(--sauce-dark) 0%, var(--sauce-deep) 50%, var(--sauce-dark) 100%);
    display: flex;
    flex-direction: column;
    align-items: center;
    padding-top: 90px;
  }
  .ornament-frame {
    position: relative;
    width: 430px;
    height: 470px;
    background: radial-gradient(circle, var(--ornament-light) 0%, #d98f86 55%, var(--ornament-red) 100%);
    display: flex;
    align-items: center;
    justify-content: center;
  }
  .title-panel {
    width: 320px;
    height: 350px;
    background: var(--panel-dark);
    display: flex;
    flex-direction: column;
    align-items: center;
    justify-content: center;
    text-align: center;
    gap: 6px;
  }
  .brand-name {
    font-family: "Oswald", sans-serif;
    font-weight: 700;
    font-size: 56px;
    line-height: 1;
    color: var(--ink-white);
    letter-spacing: 1px;
  }
  .product-type {
    font-family: "Alfa Slab One", serif;
    font-size: 104px;
    line-height: 1;
    color: var(--ink-red);
  }
  .product-word {
    font-family: "Rye", serif;
    font-size: 62px;
    line-height: 1;
    color: var(--ink-white);
    letter-spacing: 3px;
  }
  .new-tag {
    position: absolute;
    top: 40px;
    left: 20px;
    width: 70px;
    height: 46px;
    background: var(--label-red);
    transform: rotate(-14deg);
    display: flex;
    align-items: center;
    justify-content: center;
    font-family: "Oswald", sans-serif;
    font-weight: 700;
    font-size: 20px;
    color: var(--ink-white);
  }
  .net-weight {
    margin-top: 44px;
    font-family: "Oswald", sans-serif;
    font-weight: 500;
    font-size: 22px;
    letter-spacing: 2px;
    color: var(--ink-red);
  }
</style>
</head>
<body>
  <main class="canvas">
    <div class="neck-seal">
      <span class="neck-seal__name">VELQUINO</span>
    </div>
    <section class="body-label">
      <div class="ornament-frame" role="img" aria-label="Red and white decorative scroll pattern framing the product title">
        <div class="new-tag">NEW</div>
        <div class="title-panel">
          <h1 class="brand-name">VELQUINO</h1>
          <p class="product-type">BBQ</p>
          <p class="product-word">SAUCE</p>
        </div>
      </div>
      <p class="net-weight">ALL NATURAL | NET WT 16.5 OZ (467 G)</p>
    </section>
  </main>
</body>
</html>
```